Copper Lattice of Brave Movers

Hi - I would like your help transforming my (terrible) drawing into a graphic that pops -using hex colors I'll give you - so that I can put it into stationary and on t-shirts or tote bags. My company, the Tundrel Institute, trains social change leaders (from the sectors in the periodic table) on how to lead large-scale change. I have this vision - the "periodic table" but these are the sectors that my clients work in. If you are having trouble reading my writing, I apologize. Our hex colors are: #114769, #76984C, #80B5CF (Seagull), #8F2C63 and Rangoon Black #191919. You don't need to use all of them, but it'd be good to be consistent with our overall branding. If you can't read my writing, I will send correct spelling. The "Tundrel" with the flowers on the bottom is for a separate design bid.

Target Market(s)

nonprofit, social entrepreneurs, philanthropy, leaders

Requirements
Must have
• clean, readable font. alignment to look like periodic table of elements. heart icon for love, cat face for cats.

```html
<!DOCTYPE html>
<html lang="en">
<head>
<meta charset="utf-8">
<title>Copper Lattice of Brave Movers</title>
<link rel="stylesheet" href="https://fonts.googleapis.com/css2?family=Roboto:wght@400;700&family=Roboto+Condensed:wght@700&display=swap">
<style>
  :root {
    --navy: #114769;
    --green: #76984C;
    --seagull: #80B5CF;
    --plum: #8F2C63;
    --rangoon: #191919;
    --paper: #ffffff;
    --cell-w: 110.4px;
    --cell-h: 115.1px;
    --value-w: 132.5px;
  }
  * { box-sizing: border-box; margin: 0; padding: 0; }
  html, body { width: 849px; height: 1200px; overflow: hidden; background: var(--paper); }
  .poster { position: relative; width: 849px; height: 1200px; background: var(--paper); }

  .title {
    position: absolute; left: 0; right: 0; top: 70px;
    text-align: center;
    font-family: "Roboto Condensed", sans-serif; font-weight: 700;
    font-size: 53px; line-height: 1.1; letter-spacing: -0.3px;
    color: var(--plum);
  }

  .element {
    position: absolute;
    width: var(--cell-w); height: var(--cell-h);
    color: var(--paper);
    font-family: "Roboto", sans-serif;
  }
  .element .name {
    position: absolute; left: 5px; top: 10px; right: 0;
    font-size: 18px; line-height: 21px; font-weight: 400;
    white-space: nowrap;
  }
  .element .symbol {
    position: absolute; left: 5px; bottom: 9px;
    font-size: 19px; line-height: 22px; font-weight: 700;
  }
  .first .name, .first .symbol { left: 8px; }

  .navy { background: var(--navy); }
  .green { background: var(--green); }
  .seagull { background: var(--seagull); }
  .plum { background: var(--plum); }
  .rangoon { background: var(--rangoon); }

  .values-row .element { width: var(--value-w); }
  .values-row .element .name, .values-row .element .symbol { left: 8px; }
  .values-row .element .name { top: 14px; }
  .values-row .element .symbol { bottom: 11px; }

  .values-label {
    position: absolute; left: 0; right: 0; top: 722px;
    text-align: center;
    font-family: "Roboto Condensed", sans-serif; font-weight: 700;
    font-size: 44px; line-height: 1; color: var(--plum);
  }

  .brand-name {
    position: absolute; left: 0; right: 0; top: 1000px;
    text-align: center;
    font-family: "Roboto", sans-serif; font-weight: 700;
    font-size: 120px; line-height: 1;
    color: var(--plum);
  }
</style>
</head>
<body>
<main class="poster">
  <h1 class="title">Copper Lattice of Brave Movers</h1>

  <section class="table" aria-label="Sectors">
    <div class="element navy first" style="left:94.5px;top:143.1px"><span class="name">Anti<br>Violence</span><span class="symbol">Av</span></div>
    <div class="element seagull" style="left:646.7px;top:143.1px"><span class="name">Belonging</span><span class="symbol">B</span></div>

    <div class="element plum" style="left:94.5px;top:258.2px"><span class="name">Early<br>Childhood</span><span class="symbol">Ec</span></div>
    <div class="element seagull" style="left:204.9px;top:258.2px"><span class="name">Climate<br>Change</span><span class="symbol">Cc</span></div>
    <div class="element green" style="left:315.3px;top:258.2px"><span class="name">Environ-<br>mental<br>Justice</span><span class="symbol">Ej</span></div>
    <div class="element navy" style="left:425.7px;top:258.2px"><span class="name">Human<br>Senses</span><span class="symbol">Hs</span></div>
    <div class="element rangoon" style="left:536.1px;top:258.2px"><span class="name">Health<br>Care</span><span class="symbol">Hc</span></div>
    <div class="element plum" style="left:646.7px;top:258.2px"><span class="name">Housing</span><span class="symbol">H</span></div>

    <div class="element green" style="left:94.5px;top:373.3px"><span class="name">Education</span><span class="symbol">Ed</span></div>
    <div class="element navy" style="left:204.9px;top:373.3px"><span class="name">Attention<br>School</span><span class="symbol">As</span></div>
    <div class="element rangoon" style="left:315.3px;top:373.3px"><span class="name">Social<br>Justice</span><span class="symbol">Sj</span></div>
    <div class="element plum" style="left:425.7px;top:373.3px"><span class="name">Civil<br>Rights</span><span class="symbol">Cr</span></div>
    <div class="element seagull" style="left:536.1px;top:373.3px"><span class="name">Health<br>Equity</span><span class="symbol">He</span></div>
    <div class="element green" style="left:646.7px;top:373.3px"><span class="name">Jobs</span><span class="symbol">J</span></div>

    <div class="element rangoon" style="left:94.5px;top:488.4px"><span class="name">Animal<br>Welfare</span><span class="symbol">Aw</span></div>
    <div class="element plum" style="left:204.9px;top:488.4px"><span class="name">Cats</span><span class="symbol">As</span></div>
    <div class="element seagull" style="left:315.3px;top:488.4px"><span class="name">Racial<br>Justice</span><span class="symbol">Rj</span></div>
    <div class="element green" style="left:425.7px;top:488.4px"><span class="name">Immigrants’<br>Rights</span><span class="symbol">Cr</span></div>
    <div class="element navy" style="left:536.1px;top:488.4px"><span class="name">Behavioral<br>Health</span><span class="symbol">Bh</span></div>
    <div class="element rangoon" style="left:646.7px;top:488.4px"><span class="name">Inter-<br>generational</span><span class="symbol">Ig</span></div>
  </section>

  <section class="values-row" aria-label="Values">
    <div class="element plum" style="left:94.5px;top:612px"><span class="name">Love</span><span class="symbol">Aw</span></div>
    <div class="element navy" style="left:227px;top:612px"><span class="name">Authenticity</span><span class="symbol">A</span></div>
    <div class="element seagull" style="left:359.5px;top:612px"><span class="name">Humility</span><span class="symbol">Rj</span></div>
    <div class="element green" style="left:492px;top:612px"><span class="name">Audacity</span><span class="symbol">Au</span></div>
    <div class="element plum" style="left:624.5px;top:612px"><span class="name">Justice</span><span class="symbol">J</span></div>
  </section>
  <div class="values-label">VALUES</div>

  <div class="brand-name">Tundrel</div>
</main>
</body>
</html>
```